Target Market(s)

Corporate

Colors

Designer to choose colors to be used in the design.

Requirements
Must have
• An Overview / Background of the Business & Services- Company Name: ZAKI NURIFOR SMART PROJECTS W prefer as ZAKI NURI. Zaki Nuri offers specialized services in Network information security services, data center & Network infrastructure, data caption & security services, software services. Zaki Nuri provides wide range of services that helps the organization in their business priorities strategies. Zaki Nuri specialized team has handles prestigious projects & executed with ease.
• * The Target Market / Audience you are trying to reach – corporate We are doing CCTV supply & Service, cabling supply & Services , PI system supply & Service, BMS supply & Service, Fire & safety supply & services. we are basically target corporates ,malls, enterprise users and governments.
• * Design Specifics; any preferences or ideas for Style, Colour, Imagery, etc- We prefer mild & unique color.
Nice to have
• Mild and unique color

```html
<!DOCTYPE html>
<html lang="en">
<head>
<meta charset="utf-8">
<title>Zaki Nuri Network Solutions – Letterhead</title>
<link rel="stylesheet" href="https://fonts.googleapis.com/css2?family=Open+Sans:wght@400;600;700&family=Source+Sans+3:wght@400;600&family=PT+Sans:wght@400&display=swap">
<style>
  :root {
    --backdrop: #d9d9d9;
    --paper: #ffffff;
    --brand-blue: #1192d5;
    --brand-sky: #62c9ec;
    --ink: #3c3c3c;
    --ink-soft: #555555;
    --signature-tint: #dfe6f7;
  }
  * { margin: 0; padding: 0; box-sizing: border-box; }
  html, body { width: 1200px; height: 900px; overflow: hidden; }
  body {
    background: var(--backdrop);
    font-family: "Source Sans 3", sans-serif;
    color: var(--ink);
    position: relative;
  }
  .letterhead {
    position: absolute;
    left: 286px; top: 46px;
    width: 628px; height: 808px;
    background: var(--paper);
    overflow: hidden;
  }
  .header-band, .footer-band { position: absolute; left: 0; width: 628px; }
  .header-band { top: 0; height: 72px; }
  .footer-band { bottom: 0; height: 26px; }

  .brand {
    position: absolute; left: 85px; top: 86px;
    display: flex; align-items: center; gap: 12px;
  }
  .brand-dot {
    width: 34px; height: 34px; border-radius: 50%;
    background: var(--brand-blue);
  }
  .brand-name {
    font-family: "PT Sans", sans-serif;
    font-weight: 400;
    font-size: 21px; line-height: 22px;
    color: var(--brand-blue);
    letter-spacing: 0.2px;
  }

  .recipient {
    position: absolute; left: 99px; top: 205px;
    font-family: "Open Sans", sans-serif;
    font-size: 9.5px; line-height: 11px; color: var(--ink-soft);
  }
  .recipient .to-label { font-weight: 700; font-size: 11px; color: var(--ink); letter-spacing: 0.6px; }
  .recipient .to-name { font-weight: 700; color: var(--ink); letter-spacing: 0.5px; }
  .recipient .indent { padding-left: 24px; letter-spacing: 0.5px; }
  .recipient address {
    font-style: normal; font-family: "Source Sans 3", sans-serif;
    margin-top: 13px; padding-left: 24px; font-size: 9.5px; line-height: 10px;
  }
  .recipient .company { padding-left: 24px; margin-top: 4px; font-family: "Source Sans 3", sans-serif; }

  .date {
    position: absolute; right: 98px; top: 206px;
    font-family: "Open Sans", sans-serif; font-size: 9.5px;
    letter-spacing: 0.6px; color: var(--ink-soft);
  }

  .greeting {
    position: absolute; left: 99px; top: 332px;
    font-family: "Open Sans", sans-serif; font-weight: 700;
    font-size: 11px; letter-spacing: 1px; color: var(--ink);
  }
  .body-copy {
    position: absolute; left: 99px; top: 361px; width: 431px;
    font-size: 8.4px; line-height: 14px; color: var(--ink-soft);
    text-align: justify;
  }
  .body-copy p + p { margin-top: 11px; }

  .closing {
    position: absolute; left: 99px; top: 629px;
    font-size: 9.5px; color: var(--ink-soft);
  }
  .signature {
    position: absolute; left: 104px; top: 653px;
    width: 160px; height: 34px; border-radius: 4px;
    background: linear-gradient(90deg, var(--signature-tint), #eef2fb);
  }
  .signatory {
    position: absolute; left: 99px; top: 698px;
    font-size: 9.5px; line-height: 14px; color: var(--ink-soft);
  }
  .signatory strong { font-weight: 600; color: var(--ink); display: block; }
  .signatory span { font-family: "Open Sans", sans-serif; letter-spacing: 0.6px; font-size: 9.5px; }

  .contact-bar {
    position: absolute; top: 753px; left: 0; width: 628px;
    font-size: 7.4px; line-height: 10px; color: var(--ink-soft);
  }
  .contact-item { position: absolute; display: flex; gap: 9px; align-items: flex-start; }
  .contact-item svg { width: 9px; height: 9px; margin-top: 1px; flex: none; }
  .contact-item.address { left: 144px; }
  .contact-item.phone { left: 290px; }
  .contact-item.web { left: 393px; }
</style>
</head>
<body>
  <main class="letterhead">
    <svg class="header-band" viewBox="0 0 628 72" aria-hidden="true">
      <path fill="var(--brand-blue)" d="M0,0 H628 V30 L0,56 Z"/>
      <path fill="var(--brand-sky)" d="M0,62 L628,36 V42 L0,68 Z"/>
    </svg>

    <header class="brand">
      <div class="brand-dot"></div>
      <div class="brand-name">ZAKI NURI<br>NETWORK SOLUTIONS</div>
    </header>

    <section class="recipient">
      <div><span class="to-label">TO:</span> <span class="to-name">Miriam Hale</span></div>
      <div class="indent">HR Manager</div>
      <address>Office, Crescent Road #24,<br>OR, USA<br>P.O. Box 5172</address>
      <div class="company">Northwind Cargo</div>
    </section>

    <div class="date">Date: 15/1/2006</div>

    <h2 class="greeting">Dear Sir/Madam</h2>

    <article class="body-copy">
      <p>Lorem ipsum dolor sit amet, consectetu er adipiscing elit. Aenean com modo ligula eg et dol or. Aenean massa. Cum sociis natoque penatibus et magnis dis parturient montes, nascetur ridiculus mus. Donec quam felis, ultricies nec, pellentesque eu, pretium quis, sem. Nu lla consequat massa quis enim. Donec pede justo, fringilla vel, aliquet nec, vul putate eget, arcu.</p>
      <p>In enim justo, rhoncus ut, imperdiet a, venenatis vitae, justo. Lorem ipsum dolor sit amet, consectetu er adipiscing elit. Aenean com modo ligula eget dolor. Aenean massa. Cum sociis natoque penatibus et magnis dis parturient montes, nascetur ridiculus mus. Donec quam felis, ultricies nec, pellentesque eu, pretium quis, sem. Nu lla consequat massa quis enim. Donec pede justo, fringilla vel, aliquet nec, vul putate eget, arcu. In enim justo, rhoncus ut, imperdiet a, venenatis vitae, justo.</p>
      <p>Lorem ipsum dolor sit amet, consectetu er adipiscing elit. Aenean com modo ligula eget dolor. Aenean massa. Cum sociis natoque penatibus et magnis dis parturient montes, nascetur ridiculus mus. Donec quam felis, ultricies nec,</p>
      <p>Lorem ipsum dolor sit amet, consectetu er adipiscing elit. Aenean com modo ligula eget dolor. Aenean massa. Cum sociis natoque penatibus et magnis dis parturient montes, nascetur ridiculus mus. Donec quam felis, ultricies nec, pellentesque eu, pretium quis, sem. Nu lla consequat massa quis enim.</p>
    </article>

    <div class="closing">Sincerley Yours</div>
    <div class="signature" role="img" aria-label="Handwritten signature of Elias Ward"></div>
    <div class="signatory"><strong>Elias Ward</strong><span>Finance Manager</span></div>

    <footer class="contact-bar">
      <div class="contact-item address">
        <svg viewBox="0 0 10 10" aria-hidden="true"><path fill="var(--brand-blue)" d="M5,0 C2.6,0 1.2,1.7 1.2,3.6 C1.2,6.2 5,10 5,10 C5,10 8.8,6.2 8.8,3.6 C8.8,1.7 7.4,0 5,0 Z M5,2.2 A1.4,1.4 0 1 1 5,5 A1.4,1.4 0 1 1 5,2.2 Z"/></svg>
        <div>Office, Crescent Road #24, OR, USA<br>P.O. Box 5172 Harbor Point</div>
      </div>
      <div class="contact-item phone">
        <svg viewBox="0 0 10 10" aria-hidden="true"><path fill="var(--brand-blue)" d="M2,0.5 L3.6,0.5 L4.3,2.8 L3.1,3.8 C3.7,5.1 4.9,6.3 6.2,6.9 L7.2,5.7 L9.5,6.4 L9.5,8 C9.5,8.9 8.8,9.5 8,9.5 C3.8,9.2 0.8,6.2 0.5,2 C0.5,1.2 1.1,0.5 2,0.5 Z"/></svg>
        <div>001-555 014 372<br>001-555 014 372</div>
      </div>
      <div class="contact-item web">
        <svg viewBox="0 0 10 10" aria-hidden="true"><rect x="0.5" y="1" width="9" height="6" rx="0.6" fill="none" stroke="var(--brand-blue)" stroke-width="1.2"/><rect x="3.5" y="8" width="3" height="1.2" fill="var(--brand-blue)"/></svg>
        <div>hello@zakinuri.example<br>www.zakinuri.example</div>
      </div>
    </footer>

    <svg class="footer-band" viewBox="0 0 628 26" aria-hidden="true">
      <rect x="0" y="0" width="628" height="4" fill="var(--brand-sky)"/>
      <rect x="0" y="8" width="628" height="18" fill="var(--brand-blue)"/>
    </svg>
  </main>
</body>
</html>
```